Thermostat Screen Design

We need a screen layout design for a new thermostat we're currently developing. If you're not familiar with thermostats, you can see some examples here - http://smart-climate-units-guide.bestpickdigest.com/

We're after the main page design, with icons, colours etc. It needs to be clean, modern and minimalistic. Attached is all components required on the screen. The screen size is 5 inch (diagnol).

The arrows on the screen showcase what happens when you press a button. For example, when you press MODE once you get OFF, press it twice, HEAT, press it 3 times, COOL, etc. This is just for your reference.

You have complete creative license on how you choose to layout the screen, position the components etc, but we require:

- it must be on a 5 inch screen diagnol
- modern, clean and minimalistic
- includes icons and colours
- Intuitive

Let me know if any questions.

```html
<!DOCTYPE html>
<html lang="en">
<head>
<meta charset="utf-8">
<title>Thermostat Screen Design</title>
<link rel="stylesheet" href="https://fonts.googleapis.com/css2?family=Open+Sans:wght@300;400&display=swap">
<style>
  :root {
    --canvas-bg: #ece6dc;
    --text: #ffffff;
    --bar-top: rgba(38, 36, 66, 0.88);
    --bar-bottom: #1d1b22;
    --bar-mode: #141217;
    --arrow: #9a6fd0;
    --peach: #f3a07c;
    --rose: #d99ab8;
    --lilac: #a996e2;
    --periwinkle: #8b9cf2;
    --photo-top: #8f9ae8;
    --photo-mid: #d699c0;
    --photo-low: #e7a58a;
  }
  * { box-sizing: border-box; margin: 0; padding: 0; }
  html, body { width: 1200px; height: 675px; overflow: hidden; }
  body {
    background: var(--canvas-bg);
    font-family: "Open Sans", "Segoe UI", sans-serif;
    color: var(--text);
    position: relative;
  }
  .screen {
    position: absolute;
    top: 158px;
    width: 560px;
    height: 358px;
    overflow: hidden;
  }
  .screen--gradient {
    left: 20px;
    background: linear-gradient(20deg, var(--peach) 0%, var(--rose) 35%, var(--lilac) 65%, var(--periwinkle) 100%);
  }
  .screen--scenic { left: 620px; }
  .photo-placeholder {
    position: absolute;
    inset: 0;
    background: linear-gradient(180deg, var(--photo-top) 0%, var(--photo-mid) 55%, var(--photo-low) 100%);
  }
  .status-bar {
    position: absolute;
    left: 0; top: 0;
    width: 100%; height: 37px;
    background: var(--bar-top);
    font-size: 11.5px;
    line-height: 37px;
  }
  .status-bar span { position: absolute; top: 0; }
  .clock {
    position: absolute;
    left: 18px; top: 46px;
    font-size: 30px;
    font-weight: 300;
    line-height: 1.2;
    word-spacing: 16px;
  }
  .label {
    position: absolute;
    font-size: 12.5px;
    font-weight: 300;
    line-height: 1.2;
    white-space: nowrap;
  }
  .reading {
    position: absolute;
    font-weight: 300;
    line-height: 1;
    white-space: nowrap;
  }
  .reading--room { left: 114px; top: 116px; font-size: 94px; }
  .reading--outdoor { left: 432px; top: 70px; font-size: 52px; }
  .reading--humidity { left: 426px; top: 164px; font-size: 38px; }
  .unit {
    position: absolute;
    font-weight: 300;
    line-height: 1;
  }
  .unit--room { left: 203px; top: 126px; font-size: 19px; }
  .unit--outdoor { left: 488px; top: 76px; font-size: 13px; }
  .nav-bar {
    position: absolute;
    left: 0; bottom: 0;
    width: 100%; height: 55px;
    background: var(--bar-bottom);
    font-size: 12px;
    line-height: 55px;
  }
  .nav-mode {
    position: absolute;
    left: 0; top: 0;
    width: 129px; height: 55px;
    background: var(--bar-mode);
    text-align: center;
  }
  .nav-arrow { position: absolute; top: 22px; }
  .nav-item { position: absolute; top: 0; transform: translateX(-50%); }
</style>
</head>
<body>

  <section class="screen screen--gradient">
    <header class="status-bar">
      <span style="left:22px">12:14</span>
      <span style="left:121px">12/02/2014</span>
      <span style="left:248px">Wednesday</span>
      <span style="left:367px">Sleep</span>
      <span style="left:466px">Zone 02</span>
    </header>
    <div class="clock">12:14 AM</div>
    <div class="label" style="left:117px;top:106px">Room Temperature</div>
    <div class="reading reading--room">18</div>
    <div class="unit unit--room">°C</div>
    <div class="label" style="left:402px;top:57px">Outdoor Temperature</div>
    <div class="reading reading--outdoor">22</div>
    <div class="unit unit--outdoor">°C</div>
    <div class="reading reading--humidity">45%</div>
    <div class="label" style="left:432px;top:204px;font-size:11.5px">Indoor RH</div>
    <nav class="nav-bar">
      <div class="nav-mode">
        <svg class="nav-arrow" style="left:20px" width="7" height="11" viewBox="0 0 7 11"><path d="M6 0 L0 5.5 L6 11 Z" fill="var(--arrow)"/></svg>
        MODE
        <svg class="nav-arrow" style="left:101px" width="7" height="11" viewBox="0 0 7 11"><path d="M1 0 L7 5.5 L1 11 Z" fill="var(--arrow)"/></svg>
      </div>
      <span class="nav-item" style="left:187px">FAN</span>
      <span class="nav-item" style="left:323px">SETTINGS</span>
      <span class="nav-item" style="left:485px">ZONES</span>
    </nav>
  </section>

  <section class="screen screen--scenic">
    <div class="photo-placeholder" role="img" aria-label="Background photo: tropical sunset over the sea with overwater bungalows on stilts"></div>
    <header class="status-bar">
      <span style="left:22px">12:14</span>
      <span style="left:121px">12/02/2014</span>
      <span style="left:248px">Wednesday</span>
      <span style="left:367px">Sleep</span>
      <span style="left:466px">Zone 02</span>
    </header>
    <div class="clock">12:14 AM</div>
    <div class="label" style="left:117px;top:106px">Room Temperature</div>
    <div class="reading reading--room">18</div>
    <div class="unit unit--room">°C</div>
    <div class="label" style="left:402px;top:57px">Outdoor Temperature</div>
    <div class="reading reading--outdoor">22</div>
    <div class="unit unit--outdoor">°C</div>
    <div class="reading reading--humidity">45%</div>
    <div class="label" style="left:432px;top:204px;font-size:11.5px">Indoor RH</div>
    <nav class="nav-bar">
      <div class="nav-mode">
        <svg class="nav-arrow" style="left:20px" width="7" height="11" viewBox="0 0 7 11"><path d="M6 0 L0 5.5 L6 11 Z" fill="var(--arrow)"/></svg>
        MODE
        <svg class="nav-arrow" style="left:101px" width="7" height="11" viewBox="0 0 7 11"><path d="M1 0 L7 5.5 L1 11 Z" fill="var(--arrow)"/></svg>
      </div>
      <span class="nav-item" style="left:187px">FAN</span>
      <span class="nav-item" style="left:323px">SETTINGS</span>
      <span class="nav-item" style="left:485px">ZONES</span>
    </nav>
  </section>

</body>
</html>
```